e-commerce store for sport clothing online store "baseball merchandise "web application...

I want to design a UX/UI for my web application website for the online store I will provide you with the following:
1. screen shots of the initial design for the pages>
2. the logo files.
3. The brand guideline file.

the provided files (screen shots) is guideline I want to see CREATIVITY with the UX/UI DESIGN.
PS. PLEASE FOLLOW THE BRANDGUIDE LINE CAREFULLY SPECIALLY THE TYPOGRAPHY & THE COLOR CODES.

PLEASE VISIT THIS WEBSITE morningpath.velrin-qz.com to see more for the screens.

```html
<!DOCTYPE html>
<html lang="en">
<head>
<meta charset="UTF-8">
<title>Dugout Nine – Menu</title>
<link href="https://fonts.googleapis.com/css2?family=Titillium+Web:wght@400;600;700&display=swap" rel="stylesheet">
<style>
  :root{
    --navy:#0e2248;
    --page:#ffffff;
    --band:#efefef;
    --ink:#111111;
    --gold:#a89a6a;
    --muted:#8b9bbd;
    --white:#ffffff;
    --price:#b3122a;
    --banner-a:#1b0a33;
    --banner-b:#05030d;
    --shirt-a:#6f8a7a;
    --shirt-b:#3d5247;
  }
  *{margin:0;padding:0;box-sizing:border-box}
  html,body{width:1200px;height:2602px;overflow:hidden;background:var(--page);font-family:"Titillium Web",sans-serif}
  .screen{position:relative;width:1200px;height:2602px;overflow:hidden;background:var(--page)}
  .status{position:absolute;top:44px;right:40px;display:flex;align-items:center;gap:14px;font-size:36px;font-weight:600;color:var(--ink)}
  .battery{width:70px;height:32px;border:3px solid var(--ink);border-radius:8px;padding:3px;position:relative}
  .battery::after{content:"";position:absolute;right:-9px;top:9px;width:5px;height:10px;background:var(--ink);border-radius:0 3px 3px 0}
  .battery span{display:block;width:100%;height:100%;background:var(--ink);border-radius:3px}
  .cart-btn{position:absolute;left:1046px;top:228px}
  .banner{position:absolute;left:880px;top:434px;width:234px;height:634px;border-radius:60px;background:radial-gradient(circle at 30% 90%,#2a1744 0%,var(--banner-a) 40%,var(--banner-b) 100%)}
  .band{position:absolute;left:0;width:1200px;background:var(--band)}
  .chev{position:absolute;left:1090px}
  .product-img{position:absolute;border-radius:10px}
  .product-name{position:absolute;left:880px;top:1790px;font-size:42px;font-weight:400;color:var(--ink);white-space:nowrap}
  .product-price{position:absolute;left:880px;top:1915px;font-size:44px;font-weight:700;color:var(--price);white-space:nowrap}

  .drawer{position:absolute;left:0;top:0;width:916px;height:2602px;background:var(--navy);border-radius:0 92px 92px 0;color:var(--white)}
  .close{position:absolute;left:74px;top:239px}
  .brand{position:absolute;left:590px;top:244px;display:flex;align-items:center;gap:12px;font-size:36px;font-weight:700;line-height:1;color:var(--white);letter-spacing:1px;white-space:nowrap}
  .brand i{width:20px;height:20px;border-radius:50%;background:var(--white);display:block;flex:none}
  .menu{position:absolute;left:0;top:0;list-style:none}
  .menu li{position:absolute;left:66px;display:flex;align-items:center;gap:62px;font-size:50px;font-weight:700;white-space:nowrap}
  .menu li:nth-child(1){top:680px}
  .menu li:nth-child(2){top:896px}
  .connect-title{position:absolute;left:58px;top:1820px;font-size:68px;font-weight:700;color:var(--gold);white-space:nowrap}
  .contacts{position:absolute;left:0;top:0;list-style:none}
  .contacts li{position:absolute;left:62px;display:flex;align-items:center;gap:36px;font-size:40px;font-weight:600;color:var(--muted);white-space:nowrap}
  .contacts li:nth-child(1){top:2010px}
  .contacts li:nth-child(2){top:2168px}
  .contacts li:nth-child(3){top:2324px}
</style>
</head>
<body>
<div class="screen">
  <div class="status">100% <div class="battery"><span></span></div></div>

  <svg class="cart-btn" width="72" height="84" viewBox="0 0 72 84" fill="none" stroke="#111" stroke-width="6" stroke-linejoin="round">
    <path d="M22 26V18a14 14 0 0 1 28 0v8"/>
    <rect x="6" y="26" width="60" height="52" rx="14"/>
    <circle cx="24" cy="44" r="2" fill="#111"/><circle cx="48" cy="44" r="2" fill="#111"/>
  </svg>

  <div class="banner" role="img" aria-label="Featured promotion banner image"></div>

  <svg class="chev" style="top:1208px" width="28" height="40" viewBox="0 0 28 40" fill="none" stroke="#555" stroke-width="5"><path d="M6 4l16 16L6 36"/></svg>

  <div class="band" style="top:1310px;height:900px"></div>
  <div class="product-img" role="img" aria-label="Black graphic t-shirt product photo" style="left:916px;top:1390px;width:250px;height:275px;background:linear-gradient(180deg,#2a2620,#121212)"></div>
  <div class="product-name">Tide Wave Crew</div>
  <div class="product-price">19.00 KD</div>
  <svg class="chev" style="top:2086px" width="28" height="40" viewBox="0 0 28 40" fill="none" stroke="#555" stroke-width="5"><path d="M6 4l16 16L6 36"/></svg>

  <div class="band" style="top:2240px;height:362px"></div>
  <div class="product-img" role="img" aria-label="Camouflage long-sleeve shirt product photo" style="left:960px;top:2320px;width:200px;height:282px;background:linear-gradient(160deg,var(--shirt-a),var(--shirt-b))"></div>

  <nav class="drawer">
    <svg class="close" width="60" height="60" viewBox="0 0 60 60" stroke="#fff" stroke-width="6" stroke-linecap="round"><path d="M6 6l48 48M54 6L6 54"/></svg>
    <div class="brand"><i></i>DUGOUT NINE</div>

    <ul class="menu">
      <li>
        <svg width="76" height="86" viewBox="0 0 72 84" fill="none" stroke="#fff" stroke-width="5" stroke-linejoin="round"><path d="M22 26V18a14 14 0 0 1 28 0v8"/><rect x="6" y="26" width="60" height="52" rx="14"/><circle cx="24" cy="44" r="2" fill="#fff"/><circle cx="48" cy="44" r="2" fill="#fff"/></svg>
        My Cart
      </li>
      <li>
        <svg width="76" height="86" viewBox="0 0 76 86" fill="none" stroke="#fff" stroke-width="5" stroke-linejoin="round"><path d="M38 6L70 78 38 60 6 78z"/></svg>
        Track Order
      </li>
    </ul>

    <div class="connect-title">Connect with us</div>
    <ul class="contacts">
      <li>
        <svg width="54" height="54" viewBox="0 0 54 54" fill="none" stroke="#fff" stroke-width="4.5"><circle cx="27" cy="27" r="22"/><path d="M5 27h44M27 5c-8 8-8 36 0 44M27 5c8 8 8 36 0 44"/></svg>
        morningpath.kw
      </li>
      <li>
        <svg width="54" height="54" viewBox="0 0 54 54" fill="none" stroke="#fff" stroke-width="4.5"><circle cx="27" cy="27" r="22"/></svg>
        +96550001234
      </li>
      <li>
        <svg width="54" height="54" viewBox="0 0 54 54" fill="none" stroke="#fff" stroke-width="4.5" stroke-linejoin="round"><path d="M12 5l9 11-5 6c3 7 9 13 16 16l6-5 11 9-5 8C22 50 4 32 4 10z"/></svg>
        +96550001234
      </li>
    </ul>
  </nav>
</div>
</body>
</html>
```